Business card (AI file uploaded)

We need a business card design that is minimalist using existing logo (attached). Source files must be editable so we can make the same design with other names.

Screenshots included of a design I was working on to give you an idea of the style I would like. Looking for similar modern styles

Thanks

```html
<!DOCTYPE html>
<html lang="en">
<head>
<meta charset="utf-8">
<title>Marlow Law Group – Business Card</title>
<link rel="stylesheet" href="https://fonts.googleapis.com/css2?family=Cinzel:wght@500;600&family=Didact+Gothic&display=swap">
<style>
  :root {
    --page: #e4e2df;
    --card-white: #fbfbfb;
    --ink: #141414;
    --brand-red: #7c0b10;
    --back-black: #0c0c0c;
    --band-text: #f4eeee;
  }
  * { box-sizing: border-box; margin: 0; padding: 0; }
  html, body { width: 1200px; height: 871px; overflow: hidden; }
  body {
    background: var(--page);
    font-family: "Didact Gothic", "Century Gothic", sans-serif;
    color: var(--ink);
    position: relative;
  }
  .card {
    position: absolute;
    left: 290px;
    width: 620px;
    height: 354px;
    overflow: hidden;
    box-shadow: 0 6px 18px rgba(0,0,0,0.18);
  }

  /* Back side */
  .card--back { top: 56px; background: var(--back-black); }
  .card--back .brand {
    position: absolute; left: 0; right: 0; top: 96px;
    display: flex; flex-direction: column; align-items: center;
    color: var(--brand-red);
  }
  .card--back .brand-dot {
    width: 52px; height: 52px; border-radius: 50%;
    background: var(--brand-red); margin-bottom: 18px;
  }
  .card--back .brand-name {
    font-size: 40px; letter-spacing: 3px; line-height: 1;
  }
  .card--back .brand-sub {
    font-size: 26px; letter-spacing: 5px; line-height: 1.1;
  }

  /* Front side */
  .card--front { top: 462px; background: var(--card-white); }
  .holder {
    position: absolute; left: 42px; top: 92px;
    font-family: "Cinzel", "Trajan Pro", serif;
  }
  .holder-name { font-size: 17px; font-weight: 600; letter-spacing: 3px; }
  .holder-title { font-size: 11px; font-weight: 500; letter-spacing: 2.5px; margin-top: 2px; }
  .divider {
    position: absolute; left: 42px; top: 138px;
    width: 310px; height: 1px; background: var(--ink);
  }
  .contacts {
    position: absolute; left: 42px; top: 152px;
    list-style: none; font-size: 12px; letter-spacing: 2px;
  }
  .contacts li { display: flex; align-items: center; height: 21px; }
  .contacts svg { width: 12px; height: 12px; margin-right: 14px; fill: none; stroke: var(--ink); stroke-width: 1.3; }

  .card--front .brand {
    position: absolute; right: 48px; top: 58px; width: 200px;
    display: flex; flex-direction: column; align-items: center;
    color: var(--ink);
  }
  .card--front .brand-dot {
    width: 40px; height: 40px; border-radius: 50%;
    background: var(--ink); margin-bottom: 10px;
  }
  .card--front .brand-name { font-size: 32px; letter-spacing: 2px; line-height: 1; }
  .card--front .brand-sub { font-size: 21px; letter-spacing: 4px; line-height: 1.1; }

  .address-rule {
    position: absolute; right: 42px; top: 214px;
    width: 170px; height: 1px; background: var(--ink);
  }
  .address {
    position: absolute; right: 42px; top: 224px;
    font-style: normal; text-align: right;
    font-size: 12px; letter-spacing: 2.5px; line-height: 19px;
  }

  .practice-band {
    position: absolute; left: 0; right: 0; bottom: 6px; height: 40px;
    background: var(--brand-red); color: var(--band-text);
    display: flex; align-items: center; padding-left: 42px;
    font-size: 11.5px; letter-spacing: 3.5px;
  }
  .practice-band .sep { margin: 0 12px; }
  .base-strip {
    position: absolute; left: 0; right: 0; bottom: 0; height: 6px;
    background: var(--ink);
  }
</style>
</head>
<body>

  <section class="card card--back" aria-label="Business card back">
    <div class="brand">
      <span class="brand-dot"></span>
      <span class="brand-name">MARLOW</span>
      <span class="brand-sub">LAW GROUP</span>
    </div>
  </section>

  <section class="card card--front" aria-label="Business card front">
    <div class="holder">
      <p class="holder-name">DANIEL HARTWELL</p>
      <p class="holder-title">ATTORNEY AT LAW</p>
    </div>
    <div class="divider"></div>

    <ul class="contacts">
      <li>
        <svg viewBox="0 0 12 12"><path d="M2 4.5 Q6 1 10 4.5 L9 6 L7.5 5 L4.5 5 L3 6 Z"/><rect x="3" y="6.5" width="6" height="4" rx="0.8"/></svg>
        555.204.7731
      </li>
      <li>
        <svg viewBox="0 0 12 12"><rect x="2" y="4" width="8" height="6.5" rx="0.8"/><rect x="3.5" y="1.5" width="5" height="3"/><line x1="4" y1="7.5" x2="8" y2="7.5"/></svg>
        555.318.4420
      </li>
      <li>
        <svg viewBox="0 0 12 12"><rect x="1.5" y="3" width="9" height="6.5"/><path d="M1.5 3 L6 7 L10.5 3"/></svg>
        HARTWELL@MARLOWLAW
      </li>
    </ul>

    <div class="brand">
      <span class="brand-dot"></span>
      <span class="brand-name">MARLOW</span>
      <span class="brand-sub">LAW GROUP</span>
    </div>

    <div class="address-rule"></div>
    <address class="address">
      410 MERIDIAN AVE<br>
      SUITE 200 LAKEVIEW<br>
      IL 60014
    </address>

    <div class="practice-band">
      REAL ESTATE<span class="sep">|</span>BANKRUPTCY<span class="sep">|</span>SECURITY DISABILITY
    </div>
    <div class="base-strip"></div>
  </section>

</body>
</html>
```